Toy Company Needs a Web Site For a New Toy

We need a web site for a new toy called "Zippa Loop Trike". The bike is a plastic, non motorized ride on toy for kids ages 1.5 - 5 years of age. The bike is being launched in three colors, red, blue and pink, though we may include a black option too.

For the web site we want something bold and colorful that communicates fun, therefore NO dull colors like black or grey. Nothing too cluttered. We want the site to attract the attention of kids but also give the parents a sense of confidence in our professionalism as a trustworthy toy company. The home page should focus on the bike, with different views of the bike and a small write-up on some of its key features. We would also like the home page to have a video of the bike in play. A obvious link to the shopping basket must be present as well. The site must include a shopping basket and ordering system.

Attached is a screenshot of a site that has the colourfulness and playfulness that we are looking for. Please have a look.

The bike images attached are renderings from the CAD software, actual high res photos will be used when the site is developed.

The product logo is attached and MUST be used on the site. It must be BOLD and can be incorporated into the actual website design.

The site pages are:
Home
Gallery
Buy
Contact

Competitors:
www.brambleplay.example
www.quorvaride.example
I do not like either of their sites.

We only have one product at this time, so the site is to be focused on that product, not a whole catalog of products. It is really a single product with the ability to purchase.
Updates

Project Deadline Extended
Reason: I am extending this competition in order to give me more time to review each design and provide the feedback that the designers deserve.

Target Market(s)

Parents, children ages 1.5 - 5.

Industry/Entity Type

It Company

Colors
0555a3
eb1f27
9bcb3c
faed22
f78f20
f37022
e34197
a6459a
6b449b

Requirements
Must have
• Please use the logo attached, but feel free to use different colors.
Should not have
• Dull colors like black and grey

```html
<!DOCTYPE html>
<html lang="en">
<head>
<meta charset="utf-8">
<title>Zippa Loop Trike</title>
<link href="https://fonts.googleapis.com/css2?family=PT+Sans:wght@400;700&family=Open+Sans:wght@400;600&display=swap" rel="stylesheet">
<style>
:root{
  --orange:#f08a1c;
  --orange-light:#f9b25f;
  --orange-deep:#e0801d;
  --yellow:#f9b113;
  --sky:#e9f6fb;
  --blue:#2ba2d6;
  --ink:#333333;
  --paper:#ffffff;
  --panel:#f2f2f2;
  --red:#e1262b;
  --red-deep:#a8140f;
  --amber:#f39a1e;
  --cyan:#2ba2d6;
  --green:#86bd2a;
  --grass:#7fbf2e;
  --footer-ink:#5a3307;
}
*{margin:0;padding:0;box-sizing:border-box}
html,body{width:767px;height:1200px;overflow:hidden;background:var(--paper)}
body{position:relative;font-family:"Open Sans",sans-serif;color:var(--ink)}
a{text-decoration:none;color:inherit}
.abs{position:absolute}

/* header */
.hero{left:0;top:0;width:767px;height:341px;background:radial-gradient(ellipse at 45% 30%,#fbc27a 0%,var(--orange-light) 35%,var(--orange) 80%)}
.hero-ring{border:1px solid rgba(255,255,255,.35);border-radius:50%}
.navbar{left:0;top:34px;width:767px;height:25px;background:var(--sky)}
.nav{left:294px;top:34px;display:flex;font-family:"PT Sans",sans-serif;font-weight:700;font-size:13px;text-transform:uppercase}
.nav a{color:#222;display:block;height:25px;line-height:25px;padding:0 14px}
.nav a.active{background:var(--orange-deep);color:#fff;border-top:3px solid #c66b12;line-height:22px;height:27px;margin-top:-1px;width:56px;text-align:center;padding:0}
.nav a.gallery{margin-left:12px}
.account{left:505px;top:13px;font-size:8px;font-weight:600;color:#333;letter-spacing:.2px}
.cart{left:587px;top:10px;width:64px;height:38px;background:#f2d667;border-top:4px solid #6b6b6b;font-size:8px;line-height:10px;color:#333;padding:6px 0 0 6px;display:flex;gap:5px}
.cart svg{flex:none}
.brand{left:125px;top:4px;width:74px;height:76px;border-radius:50%;background:#fff;border:3px solid var(--blue);display:flex;align-items:center;justify-content:center;text-align:center}
.brand span{font-family:"PT Sans",sans-serif;font-weight:700;font-size:13px;line-height:14px;color:var(--blue)}

.bike-photo{left:148px;top:76px;width:254px;height:200px;border-radius:26px;background:linear-gradient(160deg,#e8483a 0%,var(--red) 45%,var(--red-deep) 100%);box-shadow:0 6px 14px rgba(120,40,0,.25)}
.kids-photo{left:457px;top:84px;width:138px;height:250px;border-radius:18px;background:linear-gradient(180deg,#f0c79e 0%,#d9a67a 22%,#5f8f4c 40%,#d8433a 52%,#d9c49e 72%,#6b6b6b 100%);box-shadow:0 6px 14px rgba(120,40,0,.25)}
.grass{left:0;top:278px;width:767px;height:63px;background:linear-gradient(180deg,rgba(127,191,46,0) 0%,var(--grass) 40%,#6aae24 100%)}

/* intro */
.intro{left:0;top:341px;width:767px;height:165px;background:var(--panel);border-bottom:1px solid #e2e2e2}
.pointer{left:377px;top:505px}
.video{left:120px;top:299px;width:256px;height:179px;background:#fff;border-radius:6px;box-shadow:0 2px 6px rgba(0,0,0,.25);padding:6px}
.video-screen{position:relative;width:100%;height:100%;border-radius:3px;background:radial-gradient(circle at 50% 40%,#8fd6f3 0%,#3ea9dc 55%,#1f8cc6 100%);overflow:hidden}
.video-mark{position:absolute;left:78px;top:24px;width:86px;height:86px;border-radius:50%;border:3px solid #fff;display:flex;align-items:center;justify-content:center;text-align:center;font-family:"PT Sans",sans-serif;font-weight:700;font-size:13px;line-height:14px;color:#fff}
.controls{position:absolute;left:8px;bottom:8px;width:228px;height:20px;background:#2b2b2b;border-radius:2px;display:flex;align-items:center;gap:6px;padding:0 6px 0 0;font-size:7px;color:#ddd}
.controls .play{width:34px;height:20px;background:#111;display:flex;align-items:center;justify-content:center}
.controls .track{flex:1;height:5px;background:#555;border-radius:2px;position:relative}
.controls .time{position:absolute;left:0;top:-11px;background:#fff;color:#333;padding:0 2px;font-size:6px}
.controls .hd{font-style:italic;font-weight:700;color:#4fc3f7}

.welcome{left:398px;top:352px;font-family:"PT Sans",sans-serif;font-weight:400;font-size:18px;color:#222;white-space:nowrap}
.welcome b{color:var(--blue);font-weight:700}
.tagline{left:398px;top:376px;font-size:8px;color:#555}
.points{left:398px;top:399px;width:280px;display:grid;grid-template-columns:132px 140px;row-gap:16px;list-style:none;font-family:"PT Sans",sans-serif;font-size:10px;line-height:12px;color:#333}
.points li{display:flex;gap:8px;padding-right:6px}
.num{flex:none;width:18px;height:18px;border-radius:50%;color:#fff;font-size:9px;font-weight:700;display:flex;align-items:center;justify-content:center;border:2px solid #fff;box-shadow:0 0 0 1px #ddd}
.n1{background:var(--red)}.n2{background:var(--amber)}.n3{background:var(--cyan)}.n4{background:var(--green)}

/* features */
.features-title{left:0;top:526px;width:767px;text-align:center;font-family:"PT Sans",sans-serif;font-weight:700;font-size:20px;color:#333}
.features-rule{left:114px;top:553px;width:541px;height:4px;background:#e3e3e3}
.feature-disc{width:138px;height:138px;border-radius:50%;background:#fff;box-shadow:-6px 6px 0 6px #e9e9e9,0 0 0 1px #e3e3e3}
.feature-render{position:absolute;left:14px;top:14px;width:110px;height:110px;border-radius:50%}
.r-back{background:radial-gradient(circle at 45% 40%,#e23a2e 0%,#b3150f 60%,#7a1410 100%)}
.r-front{background:radial-gradient(circle at 50% 40%,#c03ad8 0%,#8a1aa3 60%,#5e1270 100%)}
.r-tyre{background:radial-gradient(circle at 50% 45%,#d8d8d8 0%,#8a8a8a 55%,#4a4a4a 100%)}
.feature-title{font-family:"PT Sans",sans-serif;font-weight:400;font-size:15px;color:var(--blue)}
.feature-text{width:356px;font-size:7.3px;line-height:12.6px;color:#666}

/* buy band */
.buy-band{left:0;top:1014px;width:767px;height:77px;background:var(--yellow)}
.buy-notch{left:370px;top:1013px}
.buy-btn{left:317px;top:1043px;width:132px;height:31px;border-radius:4px;background:linear-gradient(180deg,#ffffff 0%,#e6e6e6 100%);box-shadow:0 2px 3px rgba(0,0,0,.25);font-family:"PT Sans",sans-serif;font-weight:700;font-size:16px;color:#333;display:flex;align-items:center;justify-content:center;letter-spacing:.3px}

/* footer */
.footer{left:0;top:1091px;width:767px;height:109px;background:var(--orange-deep)}
.foot-brand{left:146px;top:1097px;width:78px;height:78px;border-radius:50%;background:#fff;border:3px solid var(--blue);display:flex;align-items:center;justify-content:center;text-align:center;font-family:"PT Sans",sans-serif;font-weight:700;font-size:12px;line-height:13px;color:var(--blue)}
.copyright{left:118px;top:1177px;width:134px;text-align:center;font-size:6px;line-height:7px;color:var(--footer-ink)}
.foot-col h4{font-family:"PT Sans",sans-serif;font-size:12px;font-weight:700;color:var(--footer-ink);margin-bottom:6px}
.foot-col ul{list-style:none}
.foot-col li{font-size:6.5px;line-height:13.5px;color:var(--footer-ink);text-transform:uppercase}
</style>
</head>
<body>

<header>
  <div class="abs hero"></div>
  <div class="abs hero-ring" style="left:60px;top:-90px;width:420px;height:420px"></div>
  <div class="abs hero-ring" style="left:520px;top:20px;width:380px;height:380px"></div>
  <div class="abs navbar"></div>
  <nav class="abs nav">
    <a class="active" href="#">Home</a>
    <a class="gallery" href="#">Gallery</a>
    <a href="#">Buy</a>
    <a href="#">Contact</a>
  </nav>
  <div class="abs account">LOGIN &nbsp;|&nbsp; REGISTER</div>
  <a class="abs cart" href="#">
    <svg width="18" height="16" viewBox="0 0 18 16"><path d="M1 2h3l2 8h9l2-6H5" fill="none" stroke="#333" stroke-width="1.5"/><circle cx="7" cy="13" r="1.5" fill="#333"/><circle cx="14" cy="13" r="1.5" fill="#333"/></svg>
    <span>Cart<br>(0) items</span>
  </a>
  <div class="abs brand"><span>Zippa Loop Trike</span></div>
</header>

<section>
  <div class="abs grass" role="img" aria-label="Green lawn with small flowers"></div>
  <div class="abs bike-photo" role="img" aria-label="Red plastic ride-on trike render"></div>
  <div class="abs kids-photo" role="img" aria-label="Two young children standing and laughing in front of a house"></div>
  <svg class="abs" style="left:92px;top:168px" width="20" height="20" viewBox="0 0 20 20"><circle cx="10" cy="10" r="9" fill="none" stroke="#fff" stroke-width="1.5"/><path d="M11.5 6l-4 4 4 4" fill="none" stroke="#fff" stroke-width="1.8"/></svg>
  <svg class="abs" style="left:657px;top:168px" width="20" height="20" viewBox="0 0 20 20"><circle cx="10" cy="10" r="9" fill="none" stroke="#fff" stroke-width="1.5"/><path d="M8.5 6l4 4-4 4" fill="none" stroke="#fff" stroke-width="1.8"/></svg>
</section>

<section>
  <div class="abs intro"></div>
  <svg class="abs pointer" width="20" height="12" viewBox="0 0 20 12"><path d="M0 0L10 11L20 0" fill="#fff" stroke="#e2e2e2"/><rect x="0" y="-1" width="20" height="1" fill="#fff"/></svg>
  <div class="abs video">
    <div class="video-screen">
      <div class="video-mark">Zippa Loop Trike</div>
      <div class="controls">
        <div class="play"><svg width="10" height="10" viewBox="0 0 10 10"><path d="M2 1l7 4-7 4z" fill="#fff"/></svg></div>
        <div class="track"><span class="time">13:53</span></div>
        <span>|||||</span><span class="hd">HD</span>
        <svg width="8" height="8" viewBox="0 0 8 8"><path d="M0 3V0h3M5 0h3v3M8 5v3H5M3 8H0V5" fill="none" stroke="#ddd"/></svg>
      </div>
    </div>
  </div>
  <h1 class="abs welcome">WELCOME TO <b>ZIPPA LOOP TRIKE</b></h1>
  <p class="abs tagline">Lorem Ipsum is simply dummy text of the printing</p>
  <ul class="abs points">
    <li><span class="num n1">1.</span>It is a long established fact that a reader.</li>
    <li><span class="num n2">2.</span>There are many variations of passages.</li>
    <li><span class="num n3">3.</span>Contrary to popular belief, Lorem Ipsum</li>
    <li><span class="num n4">4.</span>The standard chunk of Lorem Ipsum used.</li>
  </ul>
</section>

<section>
  <h2 class="abs features-title">Our Features</h2>
  <div class="abs features-rule"></div>

  <div class="abs feature-disc" style="left:136px;top:571px"><div class="feature-render r-back" role="img" aria-label="Rear view of the red trike"></div></div>
  <h3 class="abs feature-title" style="left:295px;top:587px">Back design</h3>
  <p class="abs feature-text" style="left:296px;top:610px">Lorem Ipsum is simply dummy text of the printing and typesetting industry. Lorem Ipsum has been the industry's standard dummy text ever since the 1500s, when an unknown printer took a galley of type and scrambled it to make a type specimen book. It has survived not only five centuries, but also the leap into electronic typesetting, remaining essentially unchanged. It was popularised in the 1960s with the release of Letraset sheets containing Lorem Ipsum passages.</p>

  <h3 class="abs feature-title" style="left:125px;top:724px">Front Design</h3>
  <p class="abs feature-text" style="left:126px;top:747px">Lorem Ipsum is simply dummy text of the printing and typesetting industry. Lorem Ipsum has been the industry's standard dummy text ever since the 1500s, when an unknown printer took a galley of type and scrambled it to make a type specimen book. It has survived not only five centuries, but also the leap into electronic typesetting, remaining essentially unchanged.</p>
  <div class="abs feature-disc" style="left:508px;top:711px"><div class="feature-render r-front" role="img" aria-label="Front view of the pink trike"></div></div>

  <div class="abs feature-disc" style="left:136px;top:853px"><div class="feature-render r-tyre" role="img" aria-label="Close view of the trike tyre"></div></div>
  <h3 class="abs feature-title" style="left:295px;top:870px">Tyre</h3>
  <p class="abs feature-text" style="left:296px;top:893px">Lorem Ipsum is simply dummy text of the printing and typesetting industry. Lorem Ipsum has been the industry's standard dummy text ever since the 1500s, when an unknown printer took a galley of type and scrambled it to make a type specimen book.</p>
</section>

<section>
  <div class="abs buy-band"></div>
  <svg class="abs buy-notch" width="28" height="15" viewBox="0 0 28 15"><path d="M0 0H28L14 14z" fill="#fff"/></svg>
  <a class="abs buy-btn" href="#">BUY NOW</a>
</section>

<footer>
  <div class="abs footer"></div>
  <div class="abs foot-brand">Zippa Loop Trike</div>
  <p class="abs copyright">COPYRIGHT © 2013. ZIPPA LOOP TRIKE.<br>ALL RIGHTS RESERVED</p>
  <div class="abs foot-col" style="left:284px;top:1107px">
    <h4>Our links</h4>
    <ul><li>Home</li><li>Gallery</li><li>Buy</li><li>Contact</li></ul>
  </div>
  <div class="abs foot-col" style="left:381px;top:1107px">
    <h4>Our Biks Color</h4>
    <ul><li>Blue Bike</li><li>Black Bike</li><li>Pink Bike</li><li>Red Bike</li></ul>
  </div>
  <div class="abs foot-col" style="left:501px;top:1107px">
    <h4>Other links</h4>
    <ul><li>Terms &amp; Condition</li><li>Policy</li><li>Login</li><li>Register</li></ul>
  </div>
</footer>

</body>
</html>
```